Velorami.com - have media you dont own! Velorami the idols - Site Concept

VELORAMI those who ENTERTAIN you, who you LISTEN to, who you IDOLISE, and who you 'BORROW' from... VELORAMI the IDOLS the things that are the STARS... see brief concept at www.velorami-example.com

Looking for site concept, something new, very simple transaction, not generic website. Must also drive mobile app download call to action.

In principle, we dont care how you get your media or watch a TV series or download your favourite song, however, if you are honest and love the song/movie/servies or the star, pay them!
The solution should include anonymous/protected end user interaction and digital certificate/rights management process for end users who have media not paid for to velorami and receive an approved digital certificate from Velorami authorised by the relevant media house proving legal ownership of the digital media item (music, video, TV series/episode, movie etc...)

Basic functions:
Consumer: Mobile and Web
Personal media rights administration
1. Capture core data – Create secure and private Profile account
2. Log owned/borrowed media (media legally owned tagged and media 'borrowed' tagged, decision criteria, pledge or purchase (open to ideas, function to browse PC for media on HDD/Songbarrel or mobile, tag ones to pay for etc, capture CD's owned etc. create digital library filing system?)
3. Pledge payment for media - future payment value linked to market value, I like this, not sure I will keep it forever though, pay less? use once?
4. Purchase rights for media - payment based on market value of related media item. (quidlane, credit card or other?)
5. Media Certificate management - secure and PRIVATE distribution of the certificate (open to options here), approved by media house.

design ideas welcome, modern, fast, simple steps, engaging, with sense of privacy, we wont share data, we will just pay the media houses more! Based in Switzerland, managed by Swiss privacy law. transact with min personal data required.

Reason: The service committed to 50+ designs, most received are form one provider, all off the mark and very basic, not impressed so far, was expecting some real design thought rather than standard templates being rehashed, thats not deisgn? Hope in next days I am impressed?

Target Market(s)

Digital Media Consumer

Industry/Entity Type

Media

Number of Pages Required

5+ page

Font styles to use
Sans Serif

Requirements
Must have
• Must have privacy by design, must have simple and minimal steps taken to log and declare media items and pay, with no risk of exposure. Must have payment process, must have interface to easily load media into site, drag drop, search HDD/mobile etc.
Nice to have
• Digital certificate process and admin interaction of site and with media house, secure and trusted process to provide report and logs of payment for media to specific media house and relevant payments made and tracked.
Should not have
• complex workflows are out, complex payment methods.

```html
<!DOCTYPE html>
<html lang="en">
<head>
<meta charset="utf-8">
<title>Velorami.com</title>
<link rel="stylesheet" href="https://fonts.googleapis.com/css2?family=Roboto:wght@300;400;500;700&family=Roboto+Condensed:wght@400;700&display=swap">
<style>
:root{
  --blue:#1560d6;
  --blue-deep:#0d4fb8;
  --ink:#222;
  --muted:#8a8a8a;
  --dark:#1e1e1e;
  --darker:#161616;
  --line:#e3e3e3;
  --panel:#f2f2f2;
  --white:#fff;
}
*{box-sizing:border-box;margin:0;padding:0}
html,body{width:747px;height:1200px;overflow:hidden;background:var(--white)}
body{position:relative;font-family:"Roboto",Arial,sans-serif;color:var(--ink)}

.hero{position:absolute;left:0;top:0;width:747px;height:412px;
  background:radial-gradient(ellipse at 60% 55%,#6a6a6a 0%,#3a3a3a 40%,#1a1a1a 80%);}
.hero-photo{position:absolute;inset:0}
.site-header{position:absolute;left:0;top:0;width:100%;height:50px;display:flex;align-items:center;padding:0 62px 0 30px}
.brand{font-family:"Roboto Condensed",sans-serif;font-weight:700;font-size:20px;color:var(--white);letter-spacing:.5px}
.main-nav{margin-left:auto;display:flex;gap:16px;align-items:center}
.main-nav a{color:var(--white);text-decoration:none;font-size:9px;font-weight:500;letter-spacing:.5px}
.btn-try{background:var(--blue);padding:6px 14px;border-radius:2px;margin-left:14px}

.hero-claim{position:absolute;left:170px;top:168px;width:407px;background:var(--blue);
  color:var(--white);font-family:"Roboto Condensed",sans-serif;text-transform:uppercase;
  font-size:15px;line-height:18px;letter-spacing:.6px;text-align:center;padding:7px 12px}
.hero-title{position:absolute;left:0;top:252px;width:100%;text-align:center;color:var(--white);
  font-family:"Roboto Condensed",sans-serif;font-size:17px;letter-spacing:.6px;text-transform:uppercase}
.hero-sub{position:absolute;left:0;top:298px;width:100%;text-align:center;color:var(--white);
  font-size:9px;font-weight:700;letter-spacing:.4px;text-transform:uppercase}
.hero-arrow{position:absolute;top:212px}

.intro{position:absolute;left:62px;top:458px;width:340px}
.intro h1{font-family:"Roboto Condensed",sans-serif;font-weight:400;font-size:20px;line-height:24px;text-transform:uppercase;color:#333}
.intro .lead{margin-top:16px;color:var(--blue);font-size:10px;font-weight:500;line-height:14px;padding-bottom:18px;border-bottom:1px solid var(--line)}
.intro .body{margin-top:20px;color:var(--muted);font-size:8.5px;line-height:12px}
.btn-more{display:inline-block;margin-top:22px;background:var(--blue);color:var(--white);font-size:8px;font-weight:700;padding:5px 14px;border-radius:10px}
.intro-photo{position:absolute;left:436px;top:466px;width:212px;height:240px;
  background:linear-gradient(160deg,#a07a52 0%,#5b4632 45%,#2b2b2b 100%)}

.section-head{position:absolute;top:775px;width:282px;text-align:center}
.section-head .kicker{display:block;font-size:12px;font-weight:300;color:var(--muted)}
.section-head .title{display:block;font-family:"Roboto Condensed",sans-serif;font-size:15px;letter-spacing:.6px;color:#333}
.news-card{position:absolute;left:62px;top:833px;width:282px;height:183px;background:var(--blue);color:var(--white);text-align:center}
.news-badge{position:absolute;left:126px;top:-16px;width:30px;height:30px;border-radius:50%;background:var(--white);border:2px solid var(--blue);display:flex;align-items:center;justify-content:center}
.news-card h3{margin-top:36px;font-size:15px;font-weight:500}
.news-card p{margin:14px 26px 0;font-size:8.5px;line-height:13px;font-style:italic}
.dots{display:flex;gap:5px;justify-content:center;margin-top:22px}
.dots span{width:5px;height:5px;border-radius:50%;background:rgba(255,255,255,.5)}
.dots span:first-child{background:var(--white)}

.contact-form{position:absolute;left:403px;top:847px;width:277px;height:169px;background:var(--panel);padding:14px 18px}
.field-row{display:flex;gap:12px;margin-bottom:8px}
.field{flex:1;height:16px;background:var(--white);border:1px solid #ddd;font-size:6.5px;color:#777;padding:3px 5px}
.field.message{height:52px}
.btn-submit{display:block;margin:6px auto 0;width:46px;background:var(--dark);color:var(--white);font-size:7px;font-weight:700;text-align:center;padding:4px 0}

.site-footer{position:absolute;left:0;top:1071px;width:747px;height:129px;background:var(--dark)}
.footer-links{position:absolute;top:34px;width:100%;text-align:center;font-size:8px;color:#bbb}
.footer-links a{color:#bbb;text-decoration:none;margin:0 7px}
.footer-links a.active{color:var(--blue)}
.footer-rule{position:absolute;left:150px;top:58px;width:447px;height:1px;background:#3a3a3a}
.copyright{position:absolute;top:80px;width:100%;text-align:center;font-size:7.5px;color:#999}
.social{position:absolute;top:98px;width:100%;display:flex;gap:6px;justify-content:center}
.social span{width:5px;height:5px;border-radius:50%;background:#aaa}
</style>
</head>
<body>

<section class="hero">
  <div class="hero-photo" role="img" aria-label="Close-up photograph of an acoustic guitar in dark tones"></div>
  <header class="site-header">
    <div class="brand">VELORAMI.COM</div>
    <nav class="main-nav">
      <a href="#">HOME</a><a href="#">ABOUT US</a><a href="#">FAQ</a><a href="#">CONTACT</a>
      <a href="#" class="btn-try">TRY NOW</a>
    </nav>
  </header>
  <div class="hero-claim">Velorami those who entertain you, who you listen to, who you idolise, and who you 'borrow' from...</div>
  <div class="hero-title">Velorami the idols the things that are the stars</div>
  <div class="hero-sub">Do right: Velorami those who've entertain you</div>
  <svg class="hero-arrow" style="left:14px" width="10" height="16" viewBox="0 0 10 16"><path d="M8 2 2 8l6 6" fill="none" stroke="#fff" stroke-width="2"/></svg>
  <svg class="hero-arrow" style="right:14px" width="10" height="16" viewBox="0 0 10 16"><path d="M2 2l6 6-6 6" fill="none" stroke="#fff" stroke-width="2"/></svg>
</section>

<section class="intro">
  <h1>Time to show respect, appreciation, honour and 'whatever', just Velorami</h1>
  <p class="lead">VELORAMI your stars anonymously and receive a digital certificate validating and legalising your digital rights to the media you freely obtained or viewed online</p>
  <p class="body">An anonymous service for music, movie, TV and digital entertainment lovers, who acquire their media freely online and who would like to pay their respects to the artists they appreciate by PAYing BACK!</p>
  <span class="btn-more">MORE ›</span>
</section>
<div class="intro-photo" role="img" aria-label="Photograph of a vinyl record resting on a stack of record sleeves"></div>

<div class="section-head" style="left:62px"><span class="kicker">Latest</span><span class="title">NEWS</span></div>
<div class="section-head" style="left:403px"><span class="kicker">Contact Us</span><span class="title">FOR MORE INFORMATION</span></div>

<article class="news-card">
  <div class="news-badge">
    <svg width="14" height="14" viewBox="0 0 14 14"><rect x="2" y="2" width="10" height="10" fill="none" stroke="#1560d6" stroke-width="1.5"/><path d="M4 5h6M4 7h6M4 9h4" stroke="#1560d6" stroke-width="1"/></svg>
  </div>
  <h3>Lorem ipsum dolor</h3>
  <p>"Sed ut perspiciatis unde omnis iste natus error sit voluptatem accusantium doloremque laudantium, totam rem aperiam."</p>
  <div class="dots"><span></span><span></span></div>
</article>

<form class="contact-form">
  <div class="field-row"><div class="field">First name</div><div class="field">Last name</div></div>
  <div class="field-row"><div class="field">Phone</div><div class="field">Email</div></div>
  <div class="field-row"><div class="field message">Message</div></div>
  <span class="btn-submit">SUBMIT</span>
</form>

<footer class="site-footer">
  <div class="footer-links">
    <a href="#" class="active">Home</a>|<a href="#">Legal Stuff</a>|<a href="#">Privacy Policy</a>|<a href="#">Terms Of Use</a>|<a href="#">Contact</a>
  </div>
  <div class="footer-rule"></div>
  <div class="copyright">Copyright © 2015, website name</div>
  <div class="social"><span></span><span></span><span></span></div>
</footer>

</body>
</html>
```